Valmera is a medical device company that needs a new look for their Packaging Design

Valmera is a medical device company that needs a new look for their packaging design. It should look clean and sophisticated. The logo must not be changed. Please maintain the branding of the logo.

You may refer to the attachments for our logo and the packaging template we want designed.

Industry/Entity Type

It Company

```html
<!DOCTYPE html>
<html lang="en">
<head>
<meta charset="utf-8">
<title>Valmera Aspheric Intraocular Lens Carton</title>
<link rel="stylesheet" href="https://fonts.googleapis.com/css2?family=Roboto:wght@300;400;700&family=Roboto+Condensed:wght@700&display=swap">
<style>
  :root {
    --brand-blue: #1a6cb6;
    --line-blue: #2f74b8;
    --paper: #ffffff;
    --backdrop: #e6e7e8;
    --ink: #1d5f9f;
  }
  html, body {
    margin: 0;
    padding: 0;
    width: 1200px;
    height: 1000px;
    overflow: hidden;
    background: var(--backdrop);
  }
  .dieline { display: block; width: 1200px; height: 1000px; }
  .panel-fill { fill: var(--paper); stroke: var(--line-blue); stroke-width: 1; }
  .flap-fill { fill: var(--brand-blue); stroke: var(--line-blue); stroke-width: 1; }
  .brand-circle { fill: var(--brand-blue); }
  .wordmark { font-family: "Roboto", sans-serif; font-weight: 300; fill: var(--brand-blue); letter-spacing: 2px; }
  .wordmark.on-blue { fill: var(--paper); }
  .descriptor { font-family: "Roboto Condensed", sans-serif; font-weight: 700; fill: var(--brand-blue); font-size: 11px; }
  .descriptor.on-blue { fill: var(--paper); font-size: 11.5px; }
  .product-name { font-family: "Roboto Condensed", sans-serif; font-weight: 700; fill: var(--brand-blue); }
  .product-sub { font-family: "Roboto Condensed", sans-serif; font-weight: 700; fill: var(--brand-blue); font-size: 10px; }
  .legal { font-family: "Roboto", sans-serif; font-weight: 400; fill: var(--paper); font-size: 7px; }
  .multilang { font-family: "Roboto", sans-serif; font-weight: 400; fill: var(--ink); font-size: 6.4px; }
  .symbol { fill: none; stroke: var(--brand-blue); stroke-width: 1; }
  .symbol-label { font-family: "Roboto", sans-serif; font-weight: 700; fill: var(--brand-blue); font-size: 5px; }
</style>
</head>
<body>
<svg class="dieline" viewBox="0 0 1200 1000" xmlns="http://www.w3.org/2000/svg">
  <defs>
    <clipPath id="front-panel-clip"><rect x="598" y="192" width="364" height="255"/></clipPath>
    <clipPath id="back-panel-clip"><rect x="598" y="545" width="364" height="255"/></clipPath>
    <g id="symbol-sterile">
      <rect class="symbol" x="0" y="0" width="22" height="9"/>
      <line class="symbol" x1="15" y1="0" x2="15" y2="9"/>
      <text class="symbol-label" x="1.5" y="6.5">STERILE</text>
      <text class="symbol-label" x="16" y="6.5">EO</text>
    </g>
    <g id="symbol-caution">
      <path class="symbol" d="M6 0 L12 11 L0 11 Z"/>
      <line class="symbol" x1="6" y1="4" x2="6" y2="7.5"/>
    </g>
    <g id="symbol-no-reuse">
      <circle class="symbol" cx="6" cy="6" r="5.5"/>
      <line class="symbol" x1="2" y1="10" x2="10" y2="2"/>
      <text class="symbol-label" x="4.2" y="8" font-size="6">2</text>
    </g>
    <g id="symbol-no-resterilize">
      <circle class="symbol" cx="6" cy="6" r="5.5"/>
      <line class="symbol" x1="2" y1="10" x2="10" y2="2"/>
      <rect class="symbol" x="3.5" y="4" width="5" height="4"/>
    </g>
  </defs>

  <!-- Top closure flap -->
  <g class="top-flap">
    <path class="flap-fill" d="M598 192 L598 100 Q600 95 606 95 L954 95 Q960 95 962 100 L962 192 Z"/>
    <path class="flap-fill" d="M598 95 L532 101 Q512 103 512 122 L512 184 L598 190 Z"/>
    <path class="flap-fill" d="M962 95 L1028 101 Q1048 103 1048 122 L1048 184 L962 190 Z"/>
    <g class="manufacturer-info" transform="rotate(180 780 140)">
      <text class="legal" x="692" y="130">Northfield Lens Systems Ltd.</text>
      <text class="legal" x="692" y="140">Harlow House, Mill Lane, Kendrick, Westshire, KD4 2RT, UK</text>
      <text class="legal" x="692" y="150">Website: www.nls-lens.com   E-mail: info@nls-lens.com</text>
      <text class="legal" x="692" y="167">REV.06 ED050062615</text>
    </g>
  </g>

  <!-- Left side panel -->
  <g class="side-panel side-left">
    <path class="panel-fill" d="M598 192 L470 192 Q448 192 448 214 L448 425 Q448 447 470 447 L598 447 Z"/>
    <text class="wordmark" font-size="40" transform="translate(542 206) rotate(90)">valmera</text>
    <text class="product-name" font-size="19" transform="translate(510 206) rotate(90)">ASPHERIC</text>
    <text class="product-sub" font-size="6" transform="translate(500 206) rotate(90)">WITH 360° SQUARE EDGE</text>
    <use href="#symbol-sterile" transform="translate(512 322)"/>
    <use href="#symbol-caution" transform="translate(513 356)"/>
    <use href="#symbol-no-reuse" transform="translate(513 376)"/>
    <use href="#symbol-no-resterilize" transform="translate(513 396)"/>
    <use href="#symbol-no-resterilize" transform="translate(513 416)"/>
  </g>

  <!-- Front panel -->
  <g class="front-panel">
    <rect class="panel-fill" x="598" y="192" width="364" height="255"/>
    <circle class="brand-circle" cx="660" cy="392" r="118" clip-path="url(#front-panel-clip)"/>
    <text class="wordmark" x="656" y="256" font-size="52">valmera</text>
    <text class="descriptor" x="684" y="268">HYDROPHOBIC ACRYLIC</text>
    <text class="descriptor" x="684" y="280">INTRAOCULAR LENS</text>
    <text class="product-name" x="794" y="408" font-size="27">ASPHERIC</text>
    <text class="product-sub" x="797" y="420">WITH 360° SQUARE EDGE</text>
  </g>

  <!-- Right side panel -->
  <g class="side-panel side-right">
    <path class="panel-fill" d="M962 192 L1088 192 Q1110 192 1110 214 L1110 425 Q1110 447 1088 447 L962 447 Z"/>
    <text class="wordmark" font-size="40" transform="translate(1004 432) rotate(-90)">valmera</text>
    <text class="product-name" font-size="19" transform="translate(1037 432) rotate(-90)">ASPHERIC</text>
    <text class="product-sub" font-size="6" transform="translate(1045 432) rotate(-90)">WITH 360° SQUARE EDGE</text>
    <use href="#symbol-no-resterilize" transform="translate(1030 205)"/>
    <use href="#symbol-no-resterilize" transform="translate(1030 225)"/>
    <use href="#symbol-no-reuse" transform="translate(1030 245)"/>
    <use href="#symbol-caution" transform="translate(1030 265)"/>
    <use href="#symbol-sterile" transform="translate(1045 288) rotate(90)"/>
  </g>

  <!-- Tuck flap band -->
  <g class="tuck-band">
    <path class="flap-fill" d="M598 462 L512 462 L512 480 Q514 528 560 530 L598 530 Z"/>
    <path class="flap-fill" d="M962 462 L1048 462 L1048 480 Q1046 528 1000 530 L962 530 Z"/>
    <rect class="flap-fill" x="598" y="447" width="364" height="98"/>
    <text class="wordmark on-blue" x="616" y="498" font-size="40">valmera</text>
    <text class="descriptor on-blue" x="616" y="516">HYDROPHOBIC ACRYLIC INTRAOCULAR LENS</text>
    <text class="descriptor on-blue" x="616" y="529">ASPHERIC WITH 360° SQUARE EDGE</text>
  </g>

  <!-- Back panel -->
  <g class="back-panel">
    <rect class="panel-fill" x="598" y="545" width="364" height="255"/>
    <circle class="brand-circle" cx="664" cy="737" r="122" clip-path="url(#back-panel-clip)"/>
    <text class="product-name" x="616" y="586" font-size="26">ASPHERIC</text>
    <text class="product-sub" x="619" y="598">WITH 360° SQUARE EDGE</text>

    <g class="usage-notes">
      <text class="multilang" x="795" y="570">Contains one sterile intraocular lens</text>
      <text class="multilang" x="795" y="577">Do not use if the packaging is damaged</text>
      <text class="multilang" x="795" y="584">Do not resterilize</text>

      <text class="multilang" x="795" y="595">Bevat één steriele intraoculaire lens</text>
      <text class="multilang" x="795" y="602">Niet gebruiken als de verpakking beschadigd is</text>
      <text class="multilang" x="795" y="609">Niet opnieuw steriliseren</text>

      <text class="multilang" x="795" y="620">Contient une lentille intraoculaire stérile</text>
      <text class="multilang" x="795" y="627">Ne pas utiliser si l'emballage est endommagé</text>
      <text class="multilang" x="795" y="634">Ne pas restériliser</text>

      <text class="multilang" x="795" y="645">Enthält eine sterile intraokulare Linse</text>
      <text class="multilang" x="795" y="652">Nicht verwenden, wenn die Verpackung beschädigt ist</text>
      <text class="multilang" x="795" y="659">Nicht resterilisieren</text>

      <text class="multilang" x="795" y="670">Περιέχει έναν αποστειρωμένο ενδοφθάλμιο φακό</text>
      <text class="multilang" x="795" y="677">Μην χρησιμοποιείτε αν η συσκευασία έχει φθαρεί</text>
      <text class="multilang" x="795" y="684">Μην επαναποστειρώνετε</text>

      <text class="multilang" x="795" y="695">Contiene una lente intraoculare sterile</text>
      <text class="multilang" x="795" y="702">Non usare se la confezione è danneggiata</text>
      <text class="multilang" x="795" y="709">Non risterilizzare</text>

      <text class="multilang" x="795" y="720">Contém uma lente intra-ocular esterilizada</text>
      <text class="multilang" x="795" y="727">Não use se a embalagem está danificada</text>
      <text class="multilang" x="795" y="734">Não reesterilize</text>

      <text class="multilang" x="795" y="745">Contiene una lente intraocular estéril</text>
      <text class="multilang" x="795" y="752">No utilizar si el envase está dañado</text>
      <text class="multilang" x="795" y="759">No vuelva a esterilizar</text>
    </g>

    <g class="symbol-row">
      <use href="#symbol-sterile" transform="translate(797 768)"/>
      <use href="#symbol-caution" transform="translate(843 767)"/>
      <use href="#symbol-no-reuse" transform="translate(866 767)"/>
      <use href="#symbol-no-resterilize" transform="translate(886 767)"/>
      <use href="#symbol-no-resterilize" transform="translate(907 767)"/>
    </g>
  </g>

  <!-- Bottom glue flap -->
  <path class="flap-fill bottom-flap" d="M598 800 L962 800 L962 830 Q960 835 954 835 L606 835 Q600 835 598 830 Z"/>
</svg>
</body>
</html>
```